Veloria Energy (Alternative Energy)

We sell solar panels and geothermal heating and cooling applications.
We want to emphasize that we can offer AFFORDABLE solar and thermal heating applications.
Governmental 30% tax rebate if ordered by 2017.
Solar panels from 40 -90% efficient
Units pay for themselves
Can be used with current (existing) water and heating systems
Lower energy consumption
Great Backup Heaters in case of power outage.
100% solar powered units. Self running thermosphyin design
Low maintenance
Can be Self installed
Saves the environment
Zero Emissions
Increases homes resale value
Great for remote locations
Increases Jobs

Target Market(s)

V.E.

Industry/Entity Type

Solar

Logo Text

The future is here

Number of Pages Required

5+ page

Font styles to use
Serif

Colors
f37122
fbee3e
acd036
ffffff
000000

Requirements
Must have
• Emphasize that we can offer affordable solar and thermal heating applications
• Pays for themselves within 1-3 years
• Solar panels from 40 -90% efficient
• 100% sustainable and renewable
• Very little sun light required
Nice to have
• Very professional clean modern web design
• Needs to achieve sales results.
Should not have
• any lingo. or confusion. Must be simple and effective. Needs to achieve sales results.

```html
<!DOCTYPE html>
<html lang="en">
<head>
<meta charset="utf-8">
<title>Veloria Energy</title>
<link href="https://fonts.googleapis.com/css2?family=Open+Sans:wght@400;600;700&display=swap" rel="stylesheet">
<style>
:root{
  --orange:#f37122;
  --yellow:#fbee3e;
  --green:#acd036;
  --white:#ffffff;
  --black:#000000;
  --ink:#555555;
  --line:#d8d8d8;
}
*{box-sizing:border-box;margin:0;padding:0}
html,body{width:1200px;height:2192px;overflow:hidden;background:var(--white)}
body{font-family:"Open Sans",Arial,sans-serif;color:var(--ink);position:relative}
.abs{position:absolute}

/* header */
.header{left:0;top:0;width:1200px;height:88px;background:var(--white)}
.brand{left:40px;top:26px;font-size:34px;font-weight:400;color:var(--green);letter-spacing:.5px}
.lang{right:60px;top:8px;font-size:11px;color:#666;display:flex;align-items:center;gap:6px}
.flag{width:16px;height:11px;display:inline-block;border:1px solid #ccc}
.flag.a{background:linear-gradient(#2c4aa0 50%,#d22 50%)}
.flag.b{background:linear-gradient(90deg,#e33 33%,#fff 33% 66%,#e33 66%)}
.flag.c{background:linear-gradient(90deg,#24459a 33%,#fff 33% 66%,#e33 66%)}
.nav{left:370px;top:52px;display:flex;gap:2px;font-size:13px}
.nav a{display:block;padding:6px 16px;color:#444;text-decoration:none}
.nav a.active{color:var(--orange);border-bottom:2px solid var(--orange);background:#fff6ef}
.btn{display:inline-block;color:var(--white);font-size:12px;text-align:center;border-radius:2px}
.login{left:968px;top:54px;width:52px;height:24px;line-height:24px;background:var(--orange)}
.register{left:1028px;top:54px;width:64px;height:24px;line-height:24px;background:var(--green)}

/* hero */
.hero{left:0;top:88px;width:1200px;height:482px;background:linear-gradient(180deg,#9fd3ee 0%,#cfe9f5 45%,#a9d26a 78%,#7fb33a 100%)}
.hero-caption{left:250px;top:258px;width:610px;height:120px;background:rgba(20,30,30,.72);text-align:center;color:var(--white);padding-top:22px}
.hero-caption h1{font-size:34px;font-weight:700;letter-spacing:1px}
.hero-caption p{font-size:19px;font-style:italic;color:var(--yellow);margin-top:4px}
.dots{left:560px;top:546px;display:flex;gap:8px}
.dots span{width:10px;height:10px;border-radius:50%;background:rgba(255,255,255,.6)}
.dots span.on{background:var(--white)}

/* features */
.feature{top:592px;width:356px}
.feature .pic{width:356px;height:166px}
.feature h2{font-size:22px;font-weight:600;margin-top:22px}
.feature p{font-size:11.5px;line-height:18px;margin-top:8px}
.more{background:var(--orange);color:var(--white);font-size:11px;padding:5px 12px;margin-top:14px;display:inline-block}
.t-orange{color:var(--orange)}
.t-green{color:var(--green)}

/* welcome */
.welcome{left:0;top:950px;width:1200px;text-align:center}
.welcome h2{font-size:30px;font-weight:400;color:var(--green)}
.welcome p{width:1120px;margin:14px auto 0;font-size:11.5px;line-height:18px}

/* benefits */
.benefits{left:0;top:1120px;width:1200px;height:486px;background:linear-gradient(180deg,#2b3134 0%,#1a1f21 60%,#242a2b 100%)}
.benefits h2{position:absolute;left:40px;top:22px;font-size:26px;font-weight:600;color:var(--white)}
.benefit-list{position:absolute;left:40px;top:74px;list-style:none}
.benefit-list li{display:flex;align-items:center;gap:10px;font-size:12.5px;color:var(--white);height:25px}
.art{left:640px;top:30px;width:440px;height:426px;background:linear-gradient(160deg,#3b4a44 0%,#4f7f45 45%,#3d6f8f 100%)}

/* enquiry */
.section-title{font-size:24px;font-weight:400;color:var(--green)}
.field{position:absolute;height:34px;border:1px solid var(--line);font-size:11px;color:#888;padding:9px 10px;background:var(--white)}
.submit{background:var(--green);color:var(--white);font-size:12px;width:72px;height:26px;line-height:26px;text-align:center}
.avatar{width:96px;height:96px;border-radius:50%;background:#b08a6c;border:3px solid #eee}
.stars{color:var(--orange);font-size:14px;letter-spacing:2px}
.quote{font-size:11.5px;line-height:17px;width:400px;margin-top:4px}
.who{font-size:13px;color:var(--orange);font-weight:600;margin-top:6px}
.arrow-box{width:16px;height:16px;background:var(--green)}

/* footer */
.footer{left:0;top:1966px;width:1200px;height:226px;background:var(--black);color:#ccc}
.footer h3{font-size:14px;font-weight:600;color:var(--white);margin-bottom:10px}
.footer ul{list-style:none;font-size:11.5px;line-height:18px}
.social{display:flex;gap:8px}
.social span{width:22px;height:22px;display:block}
.copy{left:0;top:188px;width:1200px;border-top:1px solid #333;text-align:center;font-size:10.5px;color:#999;padding-top:12px}
</style>
</head>
<body>

<header class="abs header">
  <div class="abs brand">Veloria Energy</div>
  <div class="abs lang">Select your Language <span class="flag a"></span><span class="flag b"></span><span class="flag c"></span></div>
  <nav class="abs nav">
    <a class="active" href="#">Home</a><a href="#">About Us</a><a href="#">Sell</a><a href="#">Service</a><a href="#">Product</a><a href="#">Contact Us</a>
  </nav>
  <span class="abs btn login">Login</span>
  <span class="abs btn register">Register</span>
</header>

<section class="abs hero" role="img" aria-label="Hands holding a grassy globe with wind turbines and a city skyline under a blue sky"></section>
<div class="abs hero-caption">
  <h1>VELORIA ENERGY</h1>
  <p>"AFFORDABLE solar and thermal heating applications."</p>
</div>
<div class="abs dots"><span class="on"></span><span></span><span></span><span></span></div>

<article class="abs feature" style="left:40px">
  <div class="pic" role="img" aria-label="Hand placing a tick on a checklist beside wind turbines" style="background:linear-gradient(180deg,#8fc3e6,#d7ecf6 60%,#9cc46a)"></div>
  <h2 class="t-orange">About us</h2>
  <p>We help homes and businesses switch to clean power with solar panels and geothermal systems that are simple to own, easy to run and priced for every family budget today.</p>
  <span class="more">Read more</span>
</article>
<article class="abs feature" style="left:422px">
  <div class="pic" role="img" aria-label="Light bulb with a green plant inside on grass" style="background:linear-gradient(180deg,#cfe6a8,#7fb33a)"></div>
  <h2 class="t-green">What We do?</h2>
  <p>We design, supply and install affordable solar and thermal heating units that work with your existing water and heating systems and pay for themselves within one to three years.</p>
  <span class="more">Read more</span>
</article>
<article class="abs feature" style="left:806px">
  <div class="pic" role="img" aria-label="Rows of solar panels in a sunny field" style="background:linear-gradient(180deg,#7fb8e4,#b9daf0 45%,#3f6f9e 70%,#7ea84a)"></div>
  <h2 class="t-orange">Why choose us?</h2>
  <p>Our panels run from 40 to 90% efficient, need very little sunlight, are fully sustainable and renewable, and come with friendly support from a local team that knows your home.</p>
  <span class="more">Read more</span>
</article>

<section class="abs welcome">
  <h2>Welcome to Veloria Energy</h2>
  <p>Clean energy should be simple. Our solar panels and geothermal heating and cooling units lower your energy bills, reduce emissions and raise the resale value of your home. Every unit is built for low maintenance and long life, can often be self installed, and keeps working as a backup heater when the power goes out. Order before the end of 2017 to claim the governmental 30% tax rebate and start saving from the very first month.</p>
  <span class="more" style="margin-top:16px">Read more</span>
</section>

<section class="abs benefits">
  <h2>Benefits of our device</h2>
  <ul class="benefit-list">
    <li><svg width="14" height="14" viewBox="0 0 14 14"><rect width="14" height="14" fill="#acd036"/><path d="M3 7.5l2.5 2.5L11 4.5" stroke="#fff" stroke-width="2" fill="none"/></svg>Governmental 30% tax rebate if ordered by 2017</li>
    <li><svg width="14" height="14" viewBox="0 0 14 14"><rect width="14" height="14" fill="#acd036"/><path d="M3 7.5l2.5 2.5L11 4.5" stroke="#fff" stroke-width="2" fill="none"/></svg>Solar panels from 40-90% efficient</li>
    <li><svg width="14" height="14" viewBox="0 0 14 14"><rect width="14" height="14" fill="#acd036"/><path d="M3 7.5l2.5 2.5L11 4.5" stroke="#fff" stroke-width="2" fill="none"/></svg>Units pay for themselves</li>
    <li><svg width="14" height="14" viewBox="0 0 14 14"><rect width="14" height="14" fill="#acd036"/><path d="M3 7.5l2.5 2.5L11 4.5" stroke="#fff" stroke-width="2" fill="none"/></svg>Can be used with current (existing) water and heating systems</li>
    <li><svg width="14" height="14" viewBox="0 0 14 14"><rect width="14" height="14" fill="#acd036"/><path d="M3 7.5l2.5 2.5L11 4.5" stroke="#fff" stroke-width="2" fill="none"/></svg>Lower energy consumption</li>
    <li><svg width="14" height="14" viewBox="0 0 14 14"><rect width="14" height="14" fill="#acd036"/><path d="M3 7.5l2.5 2.5L11 4.5" stroke="#fff" stroke-width="2" fill="none"/></svg>Great Backup Heaters in case of power outage</li>
    <li><svg width="14" height="14" viewBox="0 0 14 14"><rect width="14" height="14" fill="#acd036"/><path d="M3 7.5l2.5 2.5L11 4.5" stroke="#fff" stroke-width="2" fill="none"/></svg>100% solar powered units. Self running thermosiphon design</li>
    <li><svg width="14" height="14" viewBox="0 0 14 14"><rect width="14" height="14" fill="#acd036"/><path d="M3 7.5l2.5 2.5L11 4.5" stroke="#fff" stroke-width="2" fill="none"/></svg>Low maintenance</li>
    <li><svg width="14" height="14" viewBox="0 0 14 14"><rect width="14" height="14" fill="#acd036"/><path d="M3 7.5l2.5 2.5L11 4.5" stroke="#fff" stroke-width="2" fill="none"/></svg>Can be Self installed</li>
    <li><svg width="14" height="14" viewBox="0 0 14 14"><rect width="14" height="14" fill="#acd036"/><path d="M3 7.5l2.5 2.5L11 4.5" stroke="#fff" stroke-width="2" fill="none"/></svg>Saves the environment</li>
    <li><svg width="14" height="14" viewBox="0 0 14 14"><rect width="14" height="14" fill="#acd036"/><path d="M3 7.5l2.5 2.5L11 4.5" stroke="#fff" stroke-width="2" fill="none"/></svg>Zero Emissions</li>
    <li><svg width="14" height="14" viewBox="0 0 14 14"><rect width="14" height="14" fill="#acd036"/><path d="M3 7.5l2.5 2.5L11 4.5" stroke="#fff" stroke-width="2" fill="none"/></svg>Increases homes resale value</li>
    <li><svg width="14" height="14" viewBox="0 0 14 14"><rect width="14" height="14" fill="#acd036"/><path d="M3 7.5l2.5 2.5L11 4.5" stroke="#fff" stroke-width="2" fill="none"/></svg>Great for remote locations</li>
    <li><svg width="14" height="14" viewBox="0 0 14 14"><rect width="14" height="14" fill="#acd036"/><path d="M3 7.5l2.5 2.5L11 4.5" stroke="#fff" stroke-width="2" fill="none"/></svg>Increases Jobs</li>
  </ul>
  <div class="abs art" role="img" aria-label="Illustration of a green earth with solar panels, wind turbines and a river"></div>
  <span class="abs more" style="left:40px;top:438px;margin:0">Read more</span>
</section>

<section class="abs" style="left:40px;top:1620px;width:500px;height:330px">
  <h2 class="section-title">Quick Enquiry</h2>
  <div class="field" style="left:0;top:50px;width:236px">First Name</div>
  <div class="field" style="left:254px;top:50px;width:236px">Last Name</div>
  <div class="field" style="left:0;top:100px;width:236px">Email</div>
  <div class="field" style="left:254px;top:100px;width:236px">Phone</div>
  <div class="field" style="left:0;top:150px;width:490px;height:76px">Message</div>
  <div class="abs submit" style="left:0;top:244px">Submit</div>
</section>

<section class="abs" style="left:590px;top:1620px;width:580px;height:330px">
  <h2 class="section-title">Our Customer's Feedback</h2>
  <div class="abs arrow-box" style="left:560px;top:6px"></div>
  <div class="abs arrow-box" style="left:560px;top:26px"></div>
  <div class="abs avatar" style="left:0;top:50px" role="img" aria-label="Customer portrait"></div>
  <div class="abs" style="left:120px;top:56px">
    <div class="stars">★★★★★</div>
    <p class="quote">The panels paid for themselves in under two years. Installation was quick and our heating bills dropped right away.</p>
    <div class="who">Dara Quill</div>
  </div>
  <div class="abs avatar" style="left:0;top:180px" role="img" aria-label="Customer portrait"></div>
  <div class="abs" style="left:120px;top:186px">
    <div class="stars">★★★★★</div>
    <p class="quote">Clean, quiet and simple to run. The backup heating kept our home warm during a long power outage.</p>
    <div class="who">Dara Quill</div>
  </div>
</section>

<footer class="abs footer">
  <div class="abs" style="left:160px;top:28px">
    <h3>Quick Links</h3>
    <ul><li>Home</li><li>About Us</li><li>Sell</li><li>Service</li><li>Product</li><li>Contact Us</li></ul>
  </div>
  <div class="abs" style="left:520px;top:28px">
    <h3>Contact Us</h3>
    <ul><li>18 Meadowlark Road</li><li>Brightvale</li><li>+1 555 0142 886</li><li>info@veloriaenergy.example</li></ul>
  </div>
  <div class="abs" style="left:920px;top:28px">
    <h3>Follow Us</h3>
    <div class="social"><span style="background:#3b5b9a"></span><span style="background:#3aa0d8"></span><span style="background:#2a7bb8"></span><span style="background:#888"></span></div>
  </div>
  <div class="abs copy">© 2017 Veloria Energy. All rights reserved.</div>
</footer>

</body>
</html>
```